Buch-/E-Book-Cover für alleinreisende Frauen mit Kind
Zielgruppe
Ich bin als freiberuflicher Autor tätig und möchte mein erstes E-Book für Frauen veröffentlichen, die alleine mit ihrem Kind/ihren Kindern die Welt bereisen möchten. Meine Zielgruppe sind also abenteuerlustige Singlemütter zwischen 30 und 50, die keinen konventionellen Urlaub auf dem Bauernhof oder im All-Inclusive-Hotel verbringen möchten, sondern lieber auf eigene Faust eine Rundreise durch fremde Länder planen. In diesem Buch geht es um die Planung einer Reise nach Namibia und Tipps für die Reise selbst, was zu beachten ist, welche Möglichkeiten man hat und was besonders beachtet werden sollte. Also kein herkömmlicher Reiseführer, sondern eine Entscheidungshilfe und Unterstützung für die Reise selbst. Ich möchte eine Buchreihe veröffentlichen, deren Name immer mit
Mit Koffer los
beginnt und dann den Namen des jeweiligen Landes (hier Namibia) beinhaltet. Als Untertitel kommt dann noch dazu:
Ratgeber für allein reisende Frauen mit Kind
Aufgabenstellung
Am liebsten hätte ich ein Cover, das zu einem Teil aus einer Comiczeichnung in Schwarz/Weiß besteht und eine Frau mit Kind zeigt. Ist aber kein Muss, ich bin offen für alle anderen Vorschläge!
Zum Comicthema:
Die Frau sollte nicht zu sexy, jung und schlank sein, sondern vielmehr die Zielgruppe um die 40 ansprechen (die Kinder sind etwa zwischen 6 und 15). Die Zeichnung sollte einfach sein und das Thema nicht zu ernst nehmen. Außerdem ist ein gewisser Wiedererkennungswert der weiblichen Comicfigur wichtig, da ich beabsichtige, sie auch für weitere Cover zu verwenden (ähnlich wie bei Pauls Notizheft). Der Rest des Covers darf gerne farbig sein, allerdings nicht zu kunterbunt.
Beispiel für eine Zeichnung:
Verzweifelte Frau, die auf einen zu vollen Koffer sitzt, aus dem Klamotten quelle (irgendwo noch das Kind integrieren)
Frau läuft mit Koffer in der einen Hand und Kind hinter sich herziehend über den Erdball
Frau sitzt im KLM-Bus, Koffer und Kind oben auf das Dach geschnallt
Natürlich sind der Fantasie keine Grenzen gesetzt, es soll das Thema grob umreißen, dabei aber auch zum Schmunzeln anregen.
Text sollte im Vordergrund stehen.
NAMIBIA
Autor: Renate Volkert

```html
<!DOCTYPE html>
<html lang="de">
<head>
<meta charset="utf-8">
<title>Mit Koffer los Namibia – Buchcover</title>
<link rel="stylesheet" href="https://fonts.googleapis.com/css2?family=Oswald:wght@600;700&family=Roboto:ital,wght@0,400;0,700;1,400&display=swap">
<style>
  :root {
    --title-red: #b0141f;
    --rule-navy: #1f2a5a;
    --rule-grey: #6b6b6b;
    --text-dark: #333333;
    --author-white: #ffffff;
    --sky-top: #ffffff;
    --sky-peach: #f6d7bd;
    --sky-orange: #f2a65e;
    --sky-haze: #c9b7a8;
    --bus-white: #ecebe8;
    --bus-red: #c8101c;
    --bus-red-deep: #a80c17;
  }
  * { margin: 0; padding: 0; box-sizing: border-box; }
  html, body {
    width: 930px; height: 1200px; overflow: hidden;
    background: #ffffff;
  }
  .cover {
    position: relative;
    width: 930px; height: 1200px;
    overflow: hidden;
  }
  .cover-photo {
    position: absolute; inset: 0;
    background: linear-gradient(180deg,
      var(--sky-top) 0%,
      var(--sky-top) 30%,
      var(--sky-peach) 44%,
      var(--sky-orange) 60%,
      var(--sky-haze) 70%,
      var(--bus-white) 72%,
      var(--bus-white) 83%,
      var(--bus-red) 84%,
      var(--bus-red-deep) 100%);
  }
  .title-block {
    position: absolute; top: 60px; left: 60px; right: 60px;
    text-align: center;
  }
  .title-main, .title-country {
    font-family: "Oswald", sans-serif;
    font-weight: 700;
    color: var(--title-red);
    text-transform: uppercase;
    line-height: 0.9;
  }
  .title-main { font-size: 150px; letter-spacing: 1px; }
  .title-connector {
    display: flex; align-items: center; gap: 22px;
    margin: 6px 0 4px;
  }
  .title-connector .rule {
    flex: 1; height: 3px; background: var(--rule-navy);
  }
  .title-connector .word {
    font-family: "Roboto", sans-serif;
    font-style: italic;
    font-size: 40px;
    color: var(--title-red);
  }
  .title-country { font-size: 232px; letter-spacing: 2px; }
  .subtitle {
    margin-top: 22px;
    border-top: 2px solid var(--rule-grey);
    border-bottom: 2px solid var(--rule-grey);
    padding: 18px 0;
    font-family: "Roboto", sans-serif;
    font-size: 27px;
    letter-spacing: 1px;
    color: var(--text-dark);
    text-transform: uppercase;
  }
  .author {
    position: absolute; left: 0; right: 0; bottom: 95px;
    text-align: center;
    font-family: "Roboto", sans-serif;
    font-weight: 700;
    font-size: 50px;
    letter-spacing: 2px;
    color: var(--author-white);
    text-transform: uppercase;
  }
</style>
</head>
<body>
  <main class="cover">
    <div class="cover-photo" role="img" aria-label="Foto: rot-weißer Kleinbus vor einem Sonnenuntergang über dem Meer"></div>
    <header class="title-block">
      <h1>
        <span class="title-main">Mit Koffer</span>
        <span class="title-connector"><span class="rule"></span><span class="word">los</span><span class="rule"></span></span>
        <span class="title-country">Namibia</span>
      </h1>
      <p class="subtitle">Ratgeber für allein reisende Frauen mit Kind</p>
    </header>
    <p class="author">Renate Volkert</p>
  </main>
</body>
</html>
```